Business Card Design using new logo

As much as we'd like to think that treating everyone equally is the best strategy for fairness, the reality is that the differences in the lives of women and men have to be taken into account to ensure that organizations, programs, services, and yes, even public policy treat women and men in ways that achieve gender equity.

That's where ParityLoom - balance insight metrics comes in. Using the data-driven tools of gender analysis, our organization can help anyone determine if gender equity is being achieved - in businesses and organizations, in the planning and implementation of programs and services, and in the development and enforcement of public policy.
Updates

Apologies for the delay - have not had time to finalize the decision.  Should be early this week - probably Tuesday.

Industry/Entity Type

Business

Requirements
Must have
• New Logo for ParityLoom
• Logo plus words "Balance Insight Metrics"

```html
<!DOCTYPE html>
<html lang="en">
<head>
<meta charset="utf-8">
<title>ParityLoom Business Card</title>
<link rel="stylesheet" href="https://fonts.googleapis.com/css2?family=Open+Sans:wght@400;600&display=swap">
<style>
  :root {
    --page-bg: #e6e6e4;
    --brand-orange: #f0891f;
    --brand-orange-deep: #e07612;
    --ink: #2b2b2b;
    --ink-soft: #4a4a4a;
    --card-white: #ffffff;
    --rule-grey: #cfcfcf;
    --band-grey: #8a8a8a;
  }
  * { box-sizing: border-box; margin: 0; padding: 0; }
  html, body {
    width: 1200px; height: 951px; overflow: hidden;
    background: var(--page-bg);
    font-family: "Open Sans", Arial, sans-serif;
    color: var(--ink);
  }
  .canvas { position: relative; width: 1200px; height: 951px; }

  .card {
    position: absolute;
    width: 640px; height: 366px;
    border-radius: 22px;
    overflow: hidden;
    box-shadow: 0 10px 24px rgba(0,0,0,0.18);
  }

  /* Front */
  .card-front {
    left: 80px; top: 70px;
    background: linear-gradient(135deg, var(--brand-orange) 0%, var(--brand-orange-deep) 100%);
  }
  .front-brand {
    position: absolute; left: 300px; top: 130px;
  }
  .brand-lockup { display: flex; align-items: center; gap: 12px; }
  .brand-dot {
    width: 34px; height: 34px; border-radius: 50%;
    background: var(--card-white);
  }
  .brand-name {
    font-weight: 400; font-size: 40px; line-height: 1; color: var(--ink);
    letter-spacing: -0.5px;
  }
  .front-tagline {
    margin-top: 26px; margin-left: 46px;
    font-size: 18px; font-weight: 400; color: var(--ink);
    letter-spacing: 0.3px;
  }

  /* Back */
  .card-back {
    left: 480px; top: 490px;
    background: var(--card-white);
  }
  .back-brand { position: absolute; left: 44px; top: 150px; }
  .back-brand .brand-dot { background: var(--brand-orange); }
  .back-brand .brand-name { font-size: 38px; }

  .divider {
    position: absolute; left: 340px; top: 40px;
    width: 1px; height: 230px;
    background: linear-gradient(to bottom, transparent, var(--rule-grey) 20%, var(--rule-grey) 80%, transparent);
  }

  .contact { position: absolute; left: 366px; top: 54px; }
  .person-name { font-size: 20px; font-weight: 600; color: var(--ink); }
  .person-role { font-size: 15px; color: var(--brand-orange); margin-top: -2px; }

  .address-row { display: flex; gap: 8px; margin-top: 36px; font-size: 16px; line-height: 1.2; color: var(--ink-soft); }
  .contact-list { list-style: none; margin-top: 20px; }
  .contact-list li {
    display: flex; align-items: center; gap: 8px;
    font-size: 16px; line-height: 1.3; color: var(--ink-soft);
  }
  .icon { width: 14px; height: 14px; flex: none; fill: var(--brand-orange); }

  .back-band {
    position: absolute; left: 0; right: 0; bottom: 0; height: 56px;
    background: linear-gradient(to bottom, var(--brand-orange), var(--brand-orange-deep));
  }
  .back-band::before {
    content: ""; position: absolute; left: 0; right: 0; top: -8px; height: 5px;
    background: var(--band-grey);
  }
</style>
</head>
<body>
<main class="canvas">

  <section class="card card-front" aria-label="Card front">
    <div class="front-brand">
      <div class="brand-lockup">
        <span class="brand-dot"></span>
        <span class="brand-name">ParityLoom</span>
      </div>
      <p class="front-tagline">Balance Insight Metrics</p>
    </div>
  </section>

  <section class="card card-back" aria-label="Card back">
    <div class="back-brand">
      <div class="brand-lockup">
        <span class="brand-dot"></span>
        <span class="brand-name">ParityLoom</span>
      </div>
    </div>

    <div class="divider"></div>

    <div class="contact">
      <p class="person-name">Marcus Ellery</p>
      <p class="person-role">director</p>

      <div class="address-row">
        <svg class="icon" viewBox="0 0 14 14" aria-hidden="true"><path d="M7 1 L13 6.5 H11 V13 H8.5 V9 H5.5 V13 H3 V6.5 H1 Z"/></svg>
        <p>4100 Alder Crest Rd<br>Brenton, TX 78110</p>
      </div>

      <ul class="contact-list">
        <li>
          <svg class="icon" viewBox="0 0 14 14" aria-hidden="true"><path d="M3 1 L5.5 1 L6.5 4 L5 5.2 C5.8 7 7 8.2 8.8 9 L10 7.5 L13 8.5 V11 C13 12 12 13 11 13 C6 13 1 8 1 3 C1 2 2 1 3 1 Z"/></svg>
          555-014-2290
        </li>
        <li>
          <svg class="icon" viewBox="0 0 14 14" aria-hidden="true"><path d="M3 5 H11 V12 H3 Z M4 1 H10 V4 H4 Z"/></svg>
          555-014-2291
        </li>
        <li>
          <svg class="icon" viewBox="0 0 14 14" aria-hidden="true"><path d="M1 3 H13 V11 H1 Z M1.5 3.5 L7 8 L12.5 3.5" stroke="#fff" stroke-width="1"/></svg>
          info@parityloom.com
        </li>
        <li>
          <svg class="icon" viewBox="0 0 14 14" aria-hidden="true"><circle cx="7" cy="7" r="6"/></svg>
          www.parityloom.com
        </li>
      </ul>
    </div>

    <div class="back-band"></div>
  </section>

</main>
</body>
</html>
```